The Copperwell

We need a APP for our members. this is a Private Bar/Venue. history of the brick building is it was built in1898 and was a gentleman club, oyster house, cigar factory and then law offices before we purchased and are beginning restoration.
the APP must include
1. direct texting to the concierge
2. calendar of events
3. vantor Lock To open the lock, anyone with a code can approach the door, enable their phone's Bluetooth and press the relevant address from the app.
Read more: http://www.evenpostgazette.co.uk/sciencetech/article-4418206/farewell-metal-keys-phone-bolt-opens-front-door-without-anything-in-hand.html#ixzz9kQR2mpaL
4. Menus from various restaurants from our surrounding area
5. member name and member number to give the feel that the app is personalized
6. the members account balance
7. ability to pay their bill with credit card or quid line monthly and automatically.
8. link to züro with its own icon within the app.
9.the ability to reserve the room
Anything else that may of interest for our members that may be relevant that I may not have mentioned since we are new at this...
35 to 60 years of age
Club

```html
<!DOCTYPE html>
<html lang="en">
<head>
<meta charset="utf-8">
<title>The Copperwell — Restaurants</title>
<link href="https://fonts.googleapis.com/css2?family=Montserrat:wght@400;500&display=swap" rel="stylesheet">
<style>
:root{
  --ink:#000;
  --paper:#fff;
  --page:#ececec;
  --title:#4a4a4a;
  --muted:#8a8a8a;
  --online:#3ddc6a;
  --star:#f5d000;
  --star-off:#dcdcdc;
  --divider:#e2e2e2;
}
*{box-sizing:border-box;margin:0;padding:0}
html,body{width:675px;height:1200px;overflow:hidden}
body{background:var(--page);font-family:"Montserrat",Helvetica,Arial,sans-serif;position:relative}
.status-bar{position:absolute;top:0;left:0;width:675px;height:36px;background:var(--ink);color:var(--paper);font-size:17px;font-family:Helvetica,Arial,sans-serif}
.status-bar .carrier{position:absolute;left:6px;top:6px;display:flex;align-items:center;gap:6px}
.status-bar .time{position:absolute;left:0;right:0;top:6px;text-align:center;font-weight:600}
.status-bar .battery{position:absolute;right:10px;top:6px;display:flex;align-items:center;gap:6px}
.app-header{position:absolute;top:36px;left:0;width:675px;height:77px;background:var(--ink);color:var(--paper)}
.menu-button{position:absolute;left:31px;top:20px}
.avatar{position:absolute;left:89px;top:7px;width:50px;height:50px;border-radius:50%;background:radial-gradient(circle at 50% 45%,#8a6a52,#3b3a38);border:2px solid #555}
.member-name{position:absolute;left:154px;top:8px;font-size:22px;font-weight:400;font-family:Helvetica,Arial,sans-serif}
.member-status{position:absolute;left:155px;top:37px;font-size:16px;color:var(--online);font-family:Helvetica,Arial,sans-serif}
.balance{position:absolute;right:30px;top:17px;display:flex;align-items:center;gap:13px;font-size:21px;font-weight:600;font-family:Helvetica,Arial,sans-serif}
.tabs{position:absolute;top:126px;left:14px;width:647px;height:49px;background:var(--paper);border-radius:25px;display:flex;overflow:hidden}
.tab{display:flex;align-items:center;justify-content:center;gap:14px;font-size:19px;font-weight:500;color:#222}
.tab.is-active{background:var(--ink);color:var(--paper);border-radius:25px 0 0 25px;width:216px}
.tab.map{width:215px}
.tab.ride{flex:1;border-left:1px solid var(--divider);margin:9px 0}
.ride-dot{width:12px;height:12px;border-radius:50%;background:#222}
.restaurant-list{position:absolute;top:202px;left:14px;width:647px}
.restaurant-card{height:166px;background:var(--paper);margin-bottom:11.6px;position:relative;box-shadow:0 1px 1px rgba(0,0,0,.05)}
.restaurant-photo{position:absolute;left:12px;top:10px;width:156px;height:145px}
.restaurant-info{position:absolute;left:190px;top:14px}
.restaurant-name{font-size:26px;font-weight:500;color:var(--title);white-space:nowrap}
.restaurant-desc{font-size:16px;color:var(--muted);line-height:19px;margin-top:5px;width:395px}
.restaurant-phone{font-size:19px;color:var(--muted);margin-top:6px}
.rating{display:flex;gap:6px;margin-top:7px}
</style>
</head>
<body>
<div class="status-bar">
  <div class="carrier">
    <svg width="62" height="10"><g fill="#fff"><circle cx="5" cy="5" r="4.5"/><circle cx="17" cy="5" r="4.5"/><circle cx="29" cy="5" r="4.5"/></g><g fill="none" stroke="#fff"><circle cx="41" cy="5" r="4"/><circle cx="53" cy="5" r="4"/></g></svg>
    <span>VELLA</span>
    <svg width="18" height="14" viewBox="0 0 18 14"><path d="M9 13l2.5-3a3.5 3.5 0 0 0-5 0zM3.5 7a8 8 0 0 1 11 0l-1.6 1.8a5.6 5.6 0 0 0-7.8 0zM0.5 3.8a12.5 12.5 0 0 1 17 0L16 5.6a10 10 0 0 0-14 0z" fill="#fff"/></svg>
  </div>
  <div class="time">4:21 PM</div>
  <div class="battery">
    <svg width="10" height="16" viewBox="0 0 10 16"><path d="M1 4l8 7-4 4V1l4 4-8 7" fill="none" stroke="#888" stroke-width="1.3"/></svg>
    <span>22%</span>
    <svg width="40" height="16" viewBox="0 0 40 16"><rect x="0.5" y="0.5" width="35" height="15" rx="3" fill="none" stroke="#fff"/><rect x="2.5" y="2.5" width="7" height="11" fill="#fff"/><rect x="37" y="5" width="2" height="6" fill="#fff"/></svg>
  </div>
</div>

<header class="app-header">
  <svg class="menu-button" width="31" height="25" viewBox="0 0 31 25"><g fill="#fff"><rect y="0" width="31" height="3" rx="1"/><rect y="11" width="31" height="3" rx="1"/><rect y="22" width="31" height="3" rx="1"/></g></svg>
  <div class="avatar" role="img" aria-label="Member profile photo"></div>
  <div class="member-name">Miles Harwood</div>
  <div class="member-status">online</div>
  <div class="balance">
    <span>$1566</span>
    <svg width="30" height="28" viewBox="0 0 30 28"><path d="M4 7l16-6 2 6z" fill="#fff"/><rect x="1" y="7" width="26" height="20" rx="2" fill="#fff"/><rect x="18" y="13" width="11" height="8" rx="1.5" fill="#000"/><rect x="19.5" y="14.5" width="8" height="5" rx="1" fill="#fff"/><circle cx="22" cy="17" r="1.3" fill="#000"/></svg>
  </div>
</header>

<nav class="tabs">
  <div class="tab is-active">
    <svg width="28" height="22" viewBox="0 0 28 22"><g fill="none" stroke="#fff" stroke-width="2"><circle cx="14" cy="11" r="8"/><circle cx="14" cy="11" r="4.5"/><path d="M2 2v18M5 2v7M2 9h3M26 2c-3 2-3 7 0 8v10"/></g></svg>
    <span>Restaurants</span>
  </div>
  <div class="tab map">
    <svg width="26" height="22" viewBox="0 0 26 22"><g fill="none" stroke="#222" stroke-width="2"><path d="M13 14c-4-4-6-6.5-6-9a6 6 0 0 1 12 0c0 2.5-2 5-6 9z"/><circle cx="13" cy="5.5" r="2"/><path d="M6 13l-4 8h22l-4-8"/></g></svg>
    <span>Map</span>
  </div>
  <div class="tab ride">
    <span class="ride-dot"></span>
    <span>Züro</span>
  </div>
</nav>

<svg width="0" height="0" style="position:absolute">
  <defs><polygon id="star" points="8,0.5 10.2,5.6 15.6,6 11.4,9.5 12.8,15 8,12 3.2,15 4.6,9.5 0.4,6 5.8,5.6"/></defs>
</svg>

<main class="restaurant-list">
  <article class="restaurant-card">
    <div class="restaurant-photo" role="img" aria-label="Restaurant interior with dark wood and white chairs" style="background:linear-gradient(135deg,#3a2a1e,#8a6a48 45%,#d8cbb8 80%,#6a5a48)"></div>
    <div class="restaurant-info">
      <h2 class="restaurant-name">Lorem Ipsum is dummy text...</h2>
      <p class="restaurant-desc">Lorem Ipsum has been the industry's standard dummy text...</p>
      <p class="restaurant-phone">+1 555 014 7720</p>
      <div class="rating"><svg width="16" height="16"><use href="#star" fill="var(--star)"/></svg><svg width="16" height="16"><use href="#star" fill="var(--star)"/></svg><svg width="16" height="16"><use href="#star" fill="var(--star)"/></svg><svg width="16" height="16"><use href="#star" fill="var(--star)"/></svg><svg width="16" height="16"><use href="#star" fill="var(--star-off)"/></svg></div>
    </div>
  </article>
  <article class="restaurant-card">
    <div class="restaurant-photo" role="img" aria-label="Dining room with orange armchairs and patterned carpet" style="background:linear-gradient(170deg,#ece6dc,#d96a2a 55%,#2a3a6a)"></div>
    <div class="restaurant-info">
      <h2 class="restaurant-name">Lorem Ipsum is dummy text...</h2>
      <p class="restaurant-desc">Lorem Ipsum has been the industry's standard dummy text...</p>
      <p class="restaurant-phone">+1 555 014 7720</p>
      <div class="rating"><svg width="16" height="16"><use href="#star" fill="var(--star)"/></svg><svg width="16" height="16"><use href="#star" fill="var(--star)"/></svg><svg width="16" height="16"><use href="#star" fill="var(--star)"/></svg><svg width="16" height="16"><use href="#star" fill="var(--star)"/></svg><svg width="16" height="16"><use href="#star" fill="var(--star-off)"/></svg></div>
    </div>
  </article>
  <article class="restaurant-card">
    <div class="restaurant-photo" role="img" aria-label="Table set with glasses on a red tablecloth" style="background:linear-gradient(180deg,#9a1010,#c8202a 55%,#e8d8d8 75%,#b01820)"></div>
    <div class="restaurant-info">
      <h2 class="restaurant-name">Lorem Ipsum is dummy text...</h2>
      <p class="restaurant-desc">Lorem Ipsum has been the industry's standard dummy text...</p>
      <p class="restaurant-phone">+1 555 014 7720</p>
      <div class="rating"><svg width="16" height="16"><use href="#star" fill="var(--star)"/></svg><svg width="16" height="16"><use href="#star" fill="var(--star)"/></svg><svg width="16" height="16"><use href="#star" fill="var(--star)"/></svg><svg width="16" height="16"><use href="#star" fill="var(--star)"/></svg><svg width="16" height="16"><use href="#star" fill="var(--star-off)"/></svg></div>
    </div>
  </article>
  <article class="restaurant-card">
    <div class="restaurant-photo" role="img" aria-label="Restaurant storefront with dark awning and potted palms" style="background:linear-gradient(180deg,#2a2420,#4a3a30 50%,#6a7a3a 75%,#c8c0b0)"></div>
    <div class="restaurant-info">
      <h2 class="restaurant-name">Lorem Ipsum is dummy text...</h2>
      <p class="restaurant-desc">Lorem Ipsum has been the industry's standard dummy text...</p>
      <p class="restaurant-phone">+1 555 014 7720</p>
      <div class="rating"><svg width="16" height="16"><use href="#star" fill="var(--star)"/></svg><svg width="16" height="16"><use href="#star" fill="var(--star)"/></svg><svg width="16" height="16"><use href="#star" fill="var(--star)"/></svg><svg width="16" height="16"><use href="#star" fill="var(--star)"/></svg><svg width="16" height="16"><use href="#star" fill="var(--star-off)"/></svg></div>
    </div>
  </article>
  <article class="restaurant-card">
    <div class="restaurant-photo" role="img" aria-label="Pink dining room with banquette seating" style="background:linear-gradient(160deg,#e0a0a0,#d87a6a 45%,#c85a6a 70%,#3a2a2a)"></div>
    <div class="restaurant-info">
      <h2 class="restaurant-name">Lorem Ipsum is dummy text...</h2>
      <p class="restaurant-desc">Lorem Ipsum has been the industry's standard dummy text...</p>
      <p class="restaurant-phone">+1 555 014 7720</p>
      <div class="rating"><svg width="16" height="16"><use href="#star" fill="var(--star)"/></svg><svg width="16" height="16"><use href="#star" fill="var(--star)"/></svg><svg width="16" height="16"><use href="#star" fill="var(--star)"/></svg><svg width="16" height="16"><use href="#star" fill="var(--star)"/></svg><svg width="16" height="16"><use href="#star" fill="var(--star-off)"/></svg></div>
    </div>
  </article>
  <article class="restaurant-card">
    <div class="restaurant-photo" role="img" aria-label="Dining room with flower arrangement and warm wood ceiling" style="background:linear-gradient(180deg,#6a3a1a,#c8843a 30%,#7a8a7a 60%,#e8e8e0)"></div>
    <div class="restaurant-info">
      <h2 class="restaurant-name">Lorem Ipsum is dummy text...</h2>
      <p class="restaurant-desc">Lorem Ipsum has been the industry's standard dummy text...</p>
      <p class="restaurant-phone">+1 555 014 7720</p>
      <div class="rating"><svg width="16" height="16"><use href="#star" fill="var(--star)"/></svg><svg width="16" height="16"><use href="#star" fill="var(--star)"/></svg><svg width="16" height="16"><use href="#star" fill="var(--star)"/></svg><svg width="16" height="16"><use href="#star" fill="var(--star)"/></svg><svg width="16" height="16"><use href="#star" fill="var(--star-off)"/></svg></div>
    </div>
  </article>
</main>
</body>
</html>
```